Wealth Education Business Needs Sharp Business Card Design

We need a business card design for a recently launched investor education business called Harbor Crest.

The final design should promote security, empowerment, self improvement and financial gain. The card will ideally promote the stature of the business.

For more information and colours please visit harborcrest.com.au

Target Market(s)

Corporate executives and high net worth individuals

Industry/Entity Type

Education

Contact Information for Business Card

Name
Position
Contact Address
Phone
Mobile
Email
Website

```html
<!DOCTYPE html>
<html lang="en">
<head>
<meta charset="utf-8">
<title>Harbor Crest – Business Card</title>
<link href="https://fonts.googleapis.com/css2?family=Lato:wght@400;700;900&display=swap" rel="stylesheet">
<style>
  :root {
    --bg: #2b2b2b;
    --card: #050505;
    --teal: #19c3cc;
    --ink-dark: #0b2e33;
    --white: #f2f2f2;
    --grey: #bdbdbd;
  }
  * { margin: 0; padding: 0; box-sizing: border-box; }
  html, body { width: 1200px; height: 873px; overflow: hidden; background: var(--bg); }
  body { position: relative; font-family: "Lato", sans-serif; }

  .card {
    position: absolute;
    width: 640px; height: 366px;
    background: var(--card);
    border-radius: 18px;
    overflow: hidden;
    box-shadow: 0 14px 30px rgba(0,0,0,.55);
  }
  .card--front { left: 60px; top: 60px; }
  .card--back  { left: 500px; top: 447px; }

  .brand {
    position: absolute;
    display: flex; align-items: center; gap: 16px;
    color: var(--white);
    font-weight: 700;
    font-size: 34px;
    letter-spacing: 5px;
    text-transform: uppercase;
    white-space: nowrap;
  }
  .brand__dot { width: 22px; height: 22px; border-radius: 50%; background: var(--teal); flex: none; }
  .card--front .brand { left: 50%; top: 118px; transform: translateX(-50%); }
  .card--back .brand  { left: 50%; top: 112px; transform: translateX(-50%); }

  .programs {
    position: absolute; left: 0; right: 0; top: 276px; height: 44px;
    background: var(--teal);
    display: flex; align-items: center; justify-content: center; gap: 22px;
    color: var(--ink-dark);
    font-size: 15px; letter-spacing: .5px; text-transform: uppercase;
  }
  .programs__sep { width: 8px; height: 8px; border-radius: 50%; background: var(--ink-dark); }

  .name-band {
    position: absolute; left: 0; right: 0; top: 0; height: 64px;
    background: var(--teal);
    text-align: right; padding: 10px 30px 0 0;
  }
  .name-band__name { color: var(--white); font-weight: 900; font-size: 20px; text-transform: uppercase; line-height: 1.1; }
  .name-band__role { color: var(--ink-dark); font-size: 15px; }

  .contact-band {
    position: absolute; left: 0; right: 0; top: 250px; height: 40px;
    background: var(--teal);
  }
  .contact {
    position: absolute; top: 0; height: 40px;
    display: flex; align-items: center; justify-content: center;
    color: var(--ink-dark); font-weight: 700; font-size: 16px;
  }
  .contact--phone { left: 20px; width: 190px; }
  .contact--email { left: 210px; width: 220px; }
  .contact--web   { left: 430px; width: 200px; }
  .contact__icon {
    position: absolute; top: -19px; left: 50%; margin-left: -17px;
    width: 34px; height: 34px; border-radius: 50%;
    background: var(--white);
    display: flex; align-items: center; justify-content: center;
  }
  .contact__icon svg { width: 18px; height: 18px; }
  .contact__text { margin-top: 10px; }

  .address {
    position: absolute; left: 0; right: 0; top: 306px;
    text-align: center; color: var(--grey); font-weight: 700; font-size: 17px;
  }
</style>
</head>
<body>

<section class="card card--front" aria-label="Card front">
  <div class="brand"><span class="brand__dot"></span>Harbor Crest</div>
  <div class="programs">
    <span>Workshops</span><span class="programs__sep"></span>
    <span>Crest Traders Club</span><span class="programs__sep"></span>
    <span>Crest Investors Club</span>
  </div>
</section>

<section class="card card--back" aria-label="Card back">
  <header class="name-band">
    <div class="name-band__name">Dana Mercer</div>
    <div class="name-band__role">Director</div>
  </header>

  <div class="brand"><span class="brand__dot"></span>Harbor Crest</div>

  <div class="contact-band">
    <div class="contact contact--phone">
      <span class="contact__icon">
        <svg viewBox="0 0 24 24"><path fill="#333" d="M6.6 10.8a15 15 0 0 0 6.6 6.6l2.2-2.2a1 1 0 0 1 1-.25 11.4 11.4 0 0 0 3.6.57 1 1 0 0 1 1 1V20a1 1 0 0 1-1 1A17 17 0 0 1 3 4a1 1 0 0 1 1-1h3.5a1 1 0 0 1 1 1c0 1.25.2 2.45.57 3.6a1 1 0 0 1-.25 1z"/></svg>
      </span>
      <span class="contact__text">+1 555 014 2290</span>
    </div>
    <div class="contact contact--email">
      <span class="contact__icon">
        <svg viewBox="0 0 24 24"><rect x="3" y="6" width="18" height="12" fill="none" stroke="#333" stroke-width="2"/><path d="M3 6l9 7 9-7" fill="none" stroke="#333" stroke-width="2"/></svg>
      </span>
      <span class="contact__text">info@harborcrest.com.au</span>
    </div>
    <div class="contact contact--web">
      <span class="contact__icon">
        <svg viewBox="0 0 24 24"><path d="M10 14a4 4 0 0 0 5.7 0l3-3a4 4 0 0 0-5.7-5.7l-1 1M14 10a4 4 0 0 0-5.7 0l-3 3a4 4 0 0 0 5.7 5.7l1-1" fill="none" stroke="#333" stroke-width="2.2" stroke-linecap="round"/></svg>
      </span>
      <span class="contact__text">www.harborcrest.com.au</span>
    </div>
  </div>

  <div class="address">block 14, Lindell Avenue, Springfield</div>
</section>

</body>
</html>
```